Commercial Real Estate

We need a business card design for a new commercial real estate business that specializes in apartment building brokerage. Not individual units but the entire complex. We find and represent the owners existing buildings and well as new buyers for those buildings. The design should convey trust, integrity, knowledge and growth. It should be easily read.

Target Market(s)

40 to 65 years old

Industry/Entity Type

Real Estate

```html
<!DOCTYPE html>
<html lang="en">
<head>
<meta charset="utf-8">
<title>Brightmoor Property Investments – Business Card</title>
<link rel="stylesheet" href="https://fonts.googleapis.com/css2?family=Ubuntu:wght@400;500;700&display=swap">
<style>
  :root {
    --card-bg: #f7f7f5;
    --ink: #4a5a5c;
    --ink-dark: #1f2a2c;
    --teal: #5bb8bd;
  }
  * { margin: 0; padding: 0; box-sizing: border-box; }
  html, body {
    width: 1200px;
    height: 725px;
    overflow: hidden;
    background: var(--card-bg);
  }
  .card {
    position: relative;
    width: 1200px;
    height: 725px;
    background: var(--card-bg);
    font-family: "Ubuntu", sans-serif;
    color: var(--ink-dark);
  }

  /* Brand block */
  .brand {
    position: absolute;
    left: 100px;
    top: 150px;
    width: 402px;
    display: flex;
    flex-direction: column;
    align-items: center;
  }
  .brand-square {
    width: 120px;
    height: 120px;
    background: var(--teal);
    margin-bottom: 60px;
  }
  .brand-name {
    font-family: "Ubuntu", sans-serif;
    font-weight: 500;
    font-size: 38px;
    line-height: 1.3;
    color: var(--ink);
    text-align: center;
  }

  /* Contact block */
  .person {
    position: absolute;
    left: 614px;
    top: 192px;
  }
  .person-name {
    font-weight: 700;
    font-size: 48px;
    line-height: 1.1;
    color: var(--ink);
  }
  .person-title {
    font-weight: 400;
    font-size: 25px;
    margin-top: 8px;
    color: var(--ink-dark);
  }

  .contact-list {
    position: absolute;
    left: 612px;
    top: 325px;
    list-style: none;
  }
  .contact-item {
    display: flex;
    align-items: flex-start;
    font-size: 31px;
    line-height: 45px;
    color: var(--ink-dark);
  }
  .contact-item .icon {
    width: 32px;
    height: 45px;
    margin-right: 38px;
    flex: none;
    display: flex;
    align-items: center;
    justify-content: center;
  }
  .contact-item .icon svg { fill: var(--ink); }
  .contact-item--web { color: var(--teal); }
</style>
</head>
<body>
<main class="card">

  <section class="brand">
    <div class="brand-square" aria-hidden="true"></div>
    <p class="brand-name">Brightmoor<br>Property Investments</p>
  </section>

  <section class="person">
    <h1 class="person-name">Your Name</h1>
    <p class="person-title">Director</p>
  </section>

  <ul class="contact-list">
    <li class="contact-item">
      <span class="icon" aria-hidden="true">
        <svg width="20" height="30" viewBox="0 0 20 30"><path d="M10 0C4.5 0 0 4.4 0 9.8 0 17 10 30 10 30s10-13 10-20.2C20 4.4 15.5 0 10 0zm0 13.5a3.8 3.8 0 1 1 0-7.6 3.8 3.8 0 0 1 0 7.6z"/></svg>
      </span>
      <span>Your commercial address<br>in just two line</span>
    </li>
    <li class="contact-item">
      <span class="icon" aria-hidden="true">
        <svg width="28" height="24" viewBox="0 0 28 24"><path d="M2 7c0-3 5-5 12-5s12 2 12 5v2h-6V6.5c-2-.7-4-1-6-1s-4 .3-6 1V9H2z"/><path d="M7 10h14l4 12H3z"/><rect x="9" y="13" width="10" height="6" fill="#f7f7f5"/></svg>
      </span>
      <span>00000000000</span>
    </li>
    <li class="contact-item">
      <span class="icon" aria-hidden="true">
        <svg width="26" height="18" viewBox="0 0 26 18"><path d="M0 0h26v18H0z"/><path d="M1.5 1.5 13 10l11.5-8.5" fill="none" stroke="#f7f7f5" stroke-width="1.8"/><path d="M1.5 16.5 9.5 8.5M24.5 16.5l-8-8" fill="none" stroke="#f7f7f5" stroke-width="1.4"/></svg>
      </span>
      <span>yourname@website.com</span>
    </li>
    <li class="contact-item contact-item--web">
      <span class="icon" aria-hidden="true">
        <svg width="26" height="26" viewBox="0 0 26 26"><circle cx="13" cy="13" r="12"/><g fill="none" stroke="#f7f7f5" stroke-width="1.5"><ellipse cx="13" cy="13" rx="5" ry="12"/><path d="M1 13h24M3 7h20M3 19h20M13 1v24"/></g></svg>
      </span>
      <span>www.website.com</span>
    </li>
  </ul>

</main>
</body>
</html>
```